Meadowlyn Acres Website Design

We have been redeveloping our website already and are quite happy with the content, but the design needs to be better:
https://harvo-link.example-host.com/

Pages, content, concept etc. Can all be taken from the redeveloped website.
The farmer can register and edit/view their profile, subscribe and these pages need to be designed better as well as contact, about, pricing, tos, privacy and a page with example portlets.

We need a website to appeal to farmers, investors and retiring farmers.

The design should be clean and a little country.

We don't want any repeat designs that some may submit to every project and has no respect for the project brief, so please don't submit them.

Target Market(s)

farmers, investors, retirees

Industry/Entity Type

Farming

Number of Pages Required

5+ page

Colors

Designer to choose colors to be used in the design.

Requirements
Must have
• Nice, clean modern design that is appealing
• Profile page laid out nicely

```html
<!DOCTYPE html>
<html lang="en">
<head>
<meta charset="utf-8">
<title>Meadowlyn Acres</title>
<link rel="stylesheet" href="https://fonts.googleapis.com/css2?family=Montserrat:wght@400;500;600&family=Open+Sans:ital,wght@0,400;0,600;1,400&display=swap">
<style>
:root{
  --teal:#135f60;
  --teal-mid:#3f7f80;
  --teal-soft:#5f9596;
  --ink:#1d1d1d;
  --text:#333;
  --grey-bg:#f2f2f2;
  --white:#fff;
  --card-dark:#1f1f1f;
  --line:#d8d8d8;
}
*{box-sizing:border-box;margin:0;padding:0}
html,body{width:1200px;height:3536px;overflow:hidden}
body{position:relative;background:var(--white);font-family:'Open Sans',Arial,sans-serif;color:var(--text)}
.abs{position:absolute}
.heading{font-family:'Montserrat',Arial,sans-serif;font-weight:500;color:var(--ink);text-align:center;width:1200px;left:0;font-size:34px;letter-spacing:.5px}

/* header */
.site-header{top:0;left:0;width:1200px;height:108px;background:var(--white)}
.brand-block{top:0;left:0;width:360px;height:108px;background:var(--teal);display:flex;align-items:center;padding-left:42px;gap:18px}
.brand-dot{width:34px;height:34px;border-radius:50%;border:3px solid #9fd3c9}
.brand-name{font-family:'Montserrat',Arial,sans-serif;font-size:28px;color:var(--white);font-weight:400}
.main-nav{top:40px;left:394px;display:flex;gap:30px;font-family:'Montserrat',Arial,sans-serif;font-size:16px;color:#222}
.main-nav .active{position:relative}
.main-nav .active::after{content:"";position:absolute;left:0;right:0;bottom:-8px;height:2px;background:#222}

/* hero */
.hero{top:108px;left:0;width:1200px;height:646px;background:linear-gradient(180deg,#a8b7c0 0%,#c9b89a 45%,#5a4a32 62%,#b8923f 75%,#d7ae58 100%)}
.hero-title{top:280px;font-family:'Montserrat',Arial,sans-serif;font-weight:600;font-size:42px;color:var(--white);width:1200px;text-align:center}
.btn-hero{top:382px;left:427px;width:346px;height:75px;background:var(--teal-soft);color:var(--white);font-family:'Montserrat',Arial,sans-serif;font-weight:600;font-size:26px;display:flex;align-items:center;justify-content:center}

/* own a farm */
.intro-text{left:128px;width:950px;font-size:14px;color:#222;line-height:37px}
.path-circle{width:203px;height:203px;border-radius:50%;display:flex;align-items:flex-end;justify-content:center;padding:0 30px 42px;text-align:center;color:var(--white);font-size:13px;line-height:16px}

/* videos */
.videos{top:1273px;left:0;width:1200px;height:766px;background:var(--grey-bg)}
.video-main{top:1410px;left:85px;width:596px;height:544px;background:linear-gradient(160deg,#8f8f86 0%,#b94a3a 45%,#5b4b3e 70%,#6f7a4a 100%)}
.video-side{top:1475px;left:681px;width:245px;height:453px;background:linear-gradient(180deg,#2a2e36 0%,#3b4238 60%,#2f3a25 100%)}
.video-back{top:1549px;left:926px;width:163px;height:304px;background:linear-gradient(180deg,#262a30,#1e2418)}
.play{top:1652px;left:355px}

/* testimonials */
.testi-frame{top:2140px;left:57px;width:1086px;height:401px;border:1px solid var(--line)}
.testi-card{top:2201px;width:277px;height:375px;background:var(--white);border:3px solid var(--card-dark);border-bottom:none}
.testi-card .quote{position:absolute;top:-14px;left:50%;transform:translateX(-50%);background:var(--white);padding:0 10px;font-family:Georgia,serif;font-size:40px;line-height:34px;color:var(--teal);font-weight:bold}
.testi-card p{position:absolute;top:50px;left:18px;right:18px;font-style:italic;font-size:15px;line-height:27px;color:#222}
.testi-card .rule{position:absolute;left:22px;right:22px;bottom:78px;height:1px;background:#bbb}
.testi-card .who{position:absolute;left:-3px;right:-3px;bottom:0;height:62px;background:var(--card-dark);color:var(--white);font-size:12px;line-height:17px;text-align:center;padding-top:12px}

/* aspiring */
.aspiring{top:2576px;left:0;width:1200px;height:509px;background:var(--grey-bg)}
.step-art{top:2780px;width:130px;height:120px;border-radius:10px}
.step-btn{top:2956px;width:184px;height:47px;background:var(--teal);color:var(--white);font-family:'Montserrat',Arial,sans-serif;font-weight:600;font-size:13px;display:flex;align-items:center;justify-content:center;letter-spacing:.5px}
.dots{top:2846px;display:flex;gap:38px}
.dots span{width:7px;height:7px;border-radius:50%;background:#d6d6d6}

/* footer */
.site-footer{top:3085px;left:0;width:1200px;height:451px;background:var(--teal);color:var(--white)}
.foot-brand{top:3145px;left:42px;display:flex;align-items:center;gap:16px}
.foot-brand .brand-dot{width:36px;height:36px}
.foot-brand .brand-name{font-size:30px}
.foot-tag{top:3208px;left:90px;font-size:15px}
.foot-col{top:3272px}
.foot-col h4{font-family:'Montserrat',Arial,sans-serif;font-weight:600;font-size:20px;padding-bottom:8px;border-bottom:2px solid var(--white);display:inline-block;margin-bottom:14px}
.foot-col li{list-style:none;font-size:15px;line-height:26px}
.social{display:flex;gap:22px;margin-bottom:10px}
.social span{width:14px;height:14px;border-radius:50%;background:var(--white);display:block;margin-top:6px}
.sub-title{top:3228px;left:684px;font-family:'Montserrat',Arial,sans-serif;font-weight:500;font-size:29px}
.sub-input{top:3300px;left:667px;width:384px;height:59px;background:var(--white);color:#aaa;font-size:16px;padding:18px 22px}
.sub-btn{top:3406px;left:759px;width:203px;height:45px;border:1px solid var(--white);font-family:'Montserrat',Arial,sans-serif;font-weight:600;font-size:14px;display:flex;align-items:center;justify-content:center}
.copy{top:3505px;left:64px;font-size:12px}
</style>
</head>
<body>

<header class="abs site-header">
  <div class="abs brand-block"><span class="brand-dot"></span><span class="brand-name">Meadowlyn Acres</span></div>
  <nav class="abs main-nav">
    <span class="active">Home</span><span>Aspiring Farmers</span><span>Investors</span><span>Retiring Farmer</span><span>Blog</span><span>Pricing</span><span>Login</span>
  </nav>
</header>

<section class="abs hero" role="img" aria-label="Golden pasture with a line of trees and cattle at dusk"></section>
<h1 class="abs hero-title">Its Time to Realize Your Farming Dream</h1>
<div class="abs btn-hero">SIGN UP NOW</div>

<h2 class="abs heading" style="top:822px">You Can Own A Farm</h2>
<div class="abs intro-text" style="top:878px">We know how hard it is for a young family to find the capital required to own and operate their own farm - so we started Meadowlyn Acres.<br>We want to rejuvenate regional Australia by putting farming back up the top of the career list for anyone.</div>

<div class="abs path-circle" style="top:1002px;left:139px;background:linear-gradient(160deg,#4f6a3a,#2d3d28)" role="img" aria-label="Photo of a young farming family">We connect a young farming family</div>
<div class="abs path-circle" style="top:1002px;left:373px;background:linear-gradient(160deg,#3f6b8a,#7a2a2f)" role="img" aria-label="Photo of a retiring farming couple">With a retiring farming family</div>
<div class="abs path-circle" style="top:1002px;left:604px;background:linear-gradient(160deg,#9aa7b3,#1f2e45)" role="img" aria-label="Photo of an investor">And investors</div>
<div class="abs path-circle" style="top:1002px;left:835px;background:linear-gradient(160deg,#4a4030,#7a5a32)" role="img" aria-label="Photo of a tractor working a field">To own and operate a farm together</div>

<section class="abs videos"></section>
<h2 class="abs heading" style="top:1305px">Project Videos</h2>
<div class="abs video-back" role="img" aria-label="Video still of farm sheds at night"></div>
<div class="abs video-side" role="img" aria-label="Video still of crop rows under a dusk sky"></div>
<div class="abs video-main" role="img" aria-label="Video still of a farmer sitting with two children and a dog"></div>
<svg class="abs play" width="64" height="64" viewBox="0 0 64 64" aria-hidden="true"><circle cx="32" cy="32" r="30" fill="rgba(0,0,0,.35)" stroke="#fff" stroke-width="3"/><path d="M26 20 L44 32 L26 44 Z" fill="#fff"/></svg>

<h2 class="abs heading" style="top:2092px">Testimonials</h2>
<div class="abs testi-frame"></div>
<div class="abs testi-card" style="left:73px"><span class="quote">&ldquo;</span><p>Land access is a major barrier to growing more farmers, and we Halloways are really excited to see the development of things like Meadowlyn Acres - creative ways to assist young or emerging farmers onto land!</p><span class="rule"></span><div class="who">Wren Halloway, Halloway Farms,<br>Kinross Vale Victoria</div></div>
<div class="abs testi-card" style="left:457px"><span class="quote">&ldquo;</span><p>Meadowlyn Acres can offer an opportunity to put people with the skills and ambition, with either a farming family looking to transition into retirement or for someone who doesn't have the skills but has capital and wants somewhere safe to invest.</p><span class="rule"></span><div class="who">Wren Halloway, Halloway Farms,<br>Kinross Vale Victoria</div></div>
<div class="abs testi-card" style="left:846px"><span class="quote">&ldquo;</span><p>We both like the idea that Meadowlyn Acres could have the ability to get more young people into small rural areas. We both love rural Australia and think it's a shame so many areas are dying, as less young people take on family farms.</p><span class="rule"></span><div class="who">Wren Halloway, Halloway Farms,<br>Kinross Vale Victoria</div></div>

<section class="abs aspiring"></section>
<h2 class="abs heading" style="top:2684px">Aspiring Farmers</h2>
<div class="abs step-art" style="left:175px;background:linear-gradient(160deg,#e8eef4,#b9cde0)" role="img" aria-label="Illustration of a sign in button with a cursor"></div>
<div class="abs step-art" style="left:505px;background:linear-gradient(160deg,#f3dcc0,#e89a5a)" role="img" aria-label="Illustration of a cartoon farmer with a pitchfork"></div>
<div class="abs step-art" style="left:880px;background:linear-gradient(160deg,#f6e6a8,#d9443a 60%,#4caf50)" role="img" aria-label="Illustration of a red barn and tractor under the sun"></div>
<div class="abs dots" style="left:330px"><span></span><span></span><span></span><span></span></div>
<div class="abs dots" style="left:680px"><span></span><span></span><span></span><span></span></div>
<div class="abs step-btn" style="left:148px">REGISTER</div>
<div class="abs step-btn" style="left:478px">FARM READY</div>
<div class="abs step-btn" style="left:853px">MATCHMAKING</div>

<footer class="abs site-footer"></footer>
<div class="abs foot-brand"><span class="brand-dot"></span><span class="brand-name" style="color:#fff">Meadowlyn Acres</span></div>
<div class="abs foot-tag" style="color:#fff">It's time to realise your farming dream</div>
<div class="abs foot-col" style="left:68px;color:#fff"><h4>Pages</h4><ul><li>Farmers</li><li>Investors</li><li>Retiring</li><li>About</li><li>Pricing</li></ul></div>
<div class="abs foot-col" style="left:191px;color:#fff"><h4>Support</h4><ul><li>Contact</li><li>Terms of Service</li><li>Privacy</li><li>Newsletter</li></ul></div>
<div class="abs foot-col" style="left:346px;color:#fff"><h4>Spread the word</h4><div class="social"><span></span><span></span><span></span></div><ul><li>Donate</li></ul></div>
<div class="abs sub-title" style="color:#fff">Subscibe the Newsletter</div>
<div class="abs sub-input">E-mail</div>
<div class="abs sub-btn" style="color:#fff">SUBSCRIBE MOW</div>
<div class="abs copy" style="color:#fff">2017&copy;All Right Reserved</div>

</body>
</html>
```